We Are Corvane Marketing Collateral

We Are Corvane has undergone a rebrand with new logo, website, and intranet design builds. The business is now looking to update its marketing collateral with the new logo design and colour palette. Deliverables include PowerPoint template, Report template, Letterhead, and Email signature. Refer attached design brief for more information. Also attached are the logo and brand document.
Target Market(s)
Executive & Board of SME impact organisations.
Industry/Entity Type
We serve small to medium organisations who are delivering impact, not-for-profits, social enterprises and purpose driven organisations.
Font styles to use
Other font styles liked:
- Roca Two Thin, Rubik Regular
Look and feel
Each slider illustrates characteristics of the customer's brand and the style your logo design should communicate.

```html
<!DOCTYPE html>
<html lang="en">
<head>
<meta charset="utf-8">
<title>We Are Corvane — Letterhead</title>
<link href="https://fonts.googleapis.com/css2?family=Open+Sans:wght@300;400&family=Lora:wght@400&family=Great+Vibes&display=swap" rel="stylesheet">
<style>
  :root {
    --backdrop: #e4e4e4;
    --paper: #f3f3f3;
    --ink: #2c2c2c;
    --brand-dark: #174a45;
    --green: #3f9e6a;
    --magenta: #b0446b;
    --coral: #e35a58;
    --teal: #2a8a98;
    --orange: #e8843c;
    --rule: #c9c9c9;
  }
  * { margin: 0; padding: 0; box-sizing: border-box; }
  html, body {
    width: 1200px; height: 1200px; overflow: hidden;
    background: var(--backdrop);
  }
  .letterhead {
    position: absolute; left: 200px; top: 35px;
    width: 800px; height: 1130px;
    background: var(--paper);
    box-shadow: 0 2px 10px rgba(0,0,0,0.12);
    font-family: "Open Sans", sans-serif;
    color: var(--ink);
  }
  .colour-band {
    position: absolute; left: 0; top: 0; width: 100%; height: 12px;
    display: flex;
  }
  .colour-band span { flex: 1; }
  .colour-band .green { background: var(--green); }
  .colour-band .magenta { background: var(--magenta); }
  .colour-band .coral { background: var(--coral); }
  .colour-band .teal { background: var(--teal); }
  .colour-band .orange { background: var(--orange); }
  .colour-band .dark { background: var(--brand-dark); }

  .brand {
    position: absolute; left: 81px; top: 56px;
    display: flex; align-items: center; gap: 16px;
  }
  .brand-dot {
    width: 44px; height: 44px; border-radius: 50%;
    background: var(--teal);
  }
  .brand-name {
    font-family: "Open Sans", sans-serif;
    font-weight: 400; font-size: 34px; letter-spacing: 1px;
    color: var(--brand-dark);
  }

  .header-divider {
    position: absolute; left: 533px; top: 12px;
    width: 1px; height: 88px; background: var(--rule);
  }
  .contact {
    position: absolute; left: 550px; top: 50px;
    list-style: none;
    font-family: "Lora", serif; font-size: 13.5px; line-height: 16.5px;
    color: var(--brand-dark);
  }
  .contact li { display: flex; align-items: center; gap: 7px; }
  .contact svg { width: 10px; height: 10px; flex: none; }

  .letter-body {
    position: absolute; left: 108px; top: 266px; width: 584px;
    font-weight: 300; font-size: 13.4px; line-height: 18.8px;
  }
  .letter-body p { text-align: justify; margin-bottom: 18.8px; }
  .letter-body .salutation { margin-bottom: 18.8px; }
  .closing {
    position: absolute; left: 108px; top: 773px;
    font-weight: 300; font-size: 13.4px;
  }
  .signature {
    font-family: "Great Vibes", cursive;
    font-size: 28px; color: #1e1e1e; margin-top: 4px; margin-left: 6px;
    font-weight: 400;
  }
</style>
</head>
<body>
  <main class="letterhead">
    <div class="colour-band">
      <span class="green"></span><span class="magenta"></span><span class="coral"></span>
      <span class="teal"></span><span class="orange"></span><span class="dark"></span>
    </div>

    <div class="brand">
      <div class="brand-dot"></div>
      <div class="brand-name">CORVANE</div>
    </div>

    <div class="header-divider"></div>
    <ul class="contact">
      <li>
        <svg viewBox="0 0 10 10"><path d="M2 1 L4 1 L4.6 3 L3.5 4 Q4.5 6 6 6.5 L7 5.4 L9 6 L9 8 Q9 9 8 9 Q1 8.5 1 2 Q1 1 2 1 Z" fill="var(--orange)"/></svg>
        200.555.0147
      </li>
      <li>
        <svg viewBox="0 0 10 10"><rect x="0.5" y="2" width="9" height="6" fill="var(--orange)"/><path d="M0.5 2 L5 5.5 L9.5 2" fill="none" stroke="var(--paper)" stroke-width="0.9"/></svg>
        info@wearecorvane.com
      </li>
      <li>
        <svg viewBox="0 0 10 10"><circle cx="5" cy="5" r="4.3" fill="var(--orange)"/><path d="M0.7 5 H9.3 M5 0.7 Q2.5 5 5 9.3 M5 0.7 Q7.5 5 5 9.3" fill="none" stroke="var(--paper)" stroke-width="0.7"/></svg>
        www.wearecorvane.com
      </li>
    </ul>

    <section class="letter-body">
      <div class="salutation">Dear Daniel Harwood,</div>
      <p>Lorem ipsum dolor sit amet, consectetuer adipiscing elit, sed diam nonummy nibh euismod tincidunt ut laoreet dolore magna aliquam erat volutpat. Ut wisi enim ad minim veniam, quis nostrud exerci tation ullamcorper suscipit lobortis nisl ut aliquip ex ea commodo consequat. Duis dolore te feugait nulla facilisi. Nam liber tempor cum soluta nobis eleifend option congue nihil imperdiet doming id quod mazim placerat facer possim assum. Lorem ipsum dolor sit amet, consectetuer adipiscing elit, sed diam nonummy nibh euismod tincidunt ut laoreet dolore magna aliquam erat volutpat. Ut wisi enim ad minim veniam, quis nostrud exerci tation ullamcorper suscipit lobortis nisl ut aliquip ex ea commodo consequat.</p>
      <p>Consectetuer adipiscing elit, sed diam nonummy nibh euismod tincidunt ut laoreet dolore magna aliquam erat volutpat. Ut wisi enim ad minim veniam, quis nostrud exerci tation ullamcorper suscipit lobortis nisl ut aliquip ex ea commodo consequat. Consectetuer adipiscing elit, sed diam nonummy nibh euismod tincidunt ut laoreet dolore magna aliquam erat volutpat. Ut wisi enim ad minim veniam, quis nostrud exerci tation ullamcorper suscipit lobortis nisl ut aliquip ex ea commodo consequat.</p>
      <p>Consectetuer adipiscing elit, sed diam nonummy nibh euismod tincidunt ut laoreet dolore magna aliquam erat volutpat. Ut wisi enim ad minim veniam, quis nostrud exerci tation ullamcorper suscipit lobortis nisl ut aliquip ex ea commodo consequat. Consectetuer adipiscing elit, sed diam nonummy nibh euismod tincidunt ut laoreet dolore magna aliquam erat volutpat. Ut wisi enim ad minim veniam, quis nostrud exerci tation ullamcorper suscipit lobortis nisl ut aliquip ex ea commodo consequat.</p>
    </section>

    <div class="closing">
      <div>Sincerely Yours</div>
      <div class="signature">Thomas Ellery</div>
    </div>
  </main>
</body>
</html>
```